hi all

Im after a new age looking business card with my company logo on it

must include these details, I would like the PH and Email to be symbols

If the colours used for card could be kept within the colours used in logo that I have supplied that would be great, if another colour is to be used dark grey would be ok. no light bulbs etc thanks

Details below to be incorporated on card

Damian Holloway

Lic E871302

PH 0219647381

E info@brightvaleelectrical.example.nz

Domestic Commercial Industrial Electricians

```html
<!DOCTYPE html>
<html lang="en">
<head>
<meta charset="utf-8">
<title>Brightvale Electrical — Business Card</title>
<link href="https://fonts.googleapis.com/css2?family=Montserrat:wght@700&family=Arimo:wght@400&display=swap" rel="stylesheet">
<style>
  :root {
    --frame: #b7d7ec;
    --card-front: #0f1215;
    --card-back: #101113;
    --brand-blue: #1479c4;
    --white: #ffffff;
  }
  * { margin: 0; padding: 0; box-sizing: border-box; }
  html, body { width: 1200px; height: 1200px; overflow: hidden; background: var(--frame); }
  .canvas { position: relative; width: 1200px; height: 1200px; background: var(--frame); font-family: 'Montserrat', sans-serif; }
  .card { position: absolute; left: 12px; width: 1176px; overflow: hidden; }
  .card--front { top: 11px; height: 585px; background: var(--card-front); }
  .card--back { top: 601px; height: 585px; background: var(--card-back); }

  .brand { position: absolute; left: 115px; top: 95px; }
  .brand__ring { position: absolute; left: 128px; top: 0; width: 143px; height: 102px; border: 8px solid var(--brand-blue); border-radius: 50%; }
  .brand__name { position: absolute; left: 0; top: 119px; color: var(--brand-blue); font-weight: 700; font-size: 56px; line-height: 1; letter-spacing: 1px; white-space: nowrap; }
  .brand__sub { position: absolute; left: 192px; top: 177px; color: var(--brand-blue); font-weight: 700; font-size: 24px; line-height: 1; letter-spacing: 5px; white-space: nowrap; }

  .tagline { position: absolute; left: 115px; top: 322px; color: var(--white); font-weight: 700; font-size: 28px; line-height: 1; white-space: nowrap; }

  .person { position: absolute; left: 115px; top: 101px; }
  .person__name { font-weight: 700; font-size: 43px; line-height: 1; letter-spacing: 2px; color: var(--white); white-space: nowrap; }
  .person__first { color: var(--brand-blue); }
  .person__licence { margin-top: 10px; font-family: 'Arimo', sans-serif; font-size: 36px; line-height: 1; color: var(--brand-blue); white-space: nowrap; }

  .contact { position: absolute; left: 115px; display: flex; align-items: center; color: var(--brand-blue); font-weight: 700; font-size: 35px; line-height: 1; white-space: nowrap; }
  .contact--phone { top: 362px; }
  .contact--email { top: 446px; }
  .contact__icon { fill: var(--brand-blue); flex: none; }
  .contact--phone .contact__icon { width: 48px; height: 50px; margin-right: 22px; }
  .contact--email .contact__icon { width: 52px; height: 37px; margin-right: 18px; }
</style>
</head>
<body>
<div class="canvas">
  <section class="card card--front">
    <div class="brand">
      <span class="brand__ring"></span>
      <div class="brand__name">BRIGHTVALE</div>
      <div class="brand__sub">ELECTRICAL</div>
    </div>
    <p class="tagline">Domestic Commercial Industrial Electricians</p>
  </section>

  <section class="card card--back">
    <div class="person">
      <h1 class="person__name"><span class="person__first">DAMIAN</span> HOLLOWAY</h1>
      <p class="person__licence">Lic E871302</p>
    </div>

    <div class="contact contact--phone">
      <svg class="contact__icon" viewBox="0 0 48 50" aria-hidden="true">
        <path d="M9 1c3-2 4-1 5 1l3 6c1 2 0 3-2 4-2 1-2 3-1 5 3 5 6 9 10 12 2 1 3 1 4-1 1-2 3-3 5-2l6 3c2 1 3 3 1 5-3 4-7 6-12 4C16 43 6 32 2 20 0 11 3 5 9 1z"/>
      </svg>
      <span class="contact__text">0219647381</span>
    </div>

    <div class="contact contact--email">
      <svg class="contact__icon" viewBox="0 0 52 37" aria-hidden="true">
        <path d="M1 0h50L26 22z"/>
        <path d="M0 3l18 15L0 35z"/>
        <path d="M52 3L34 18l18 17z"/>
        <path d="M2 37l18-15 6 5 6-5 18 15z"/>
      </svg>
      <span class="contact__text">info@brightvaleelectrical.example.nz</span>
    </div>
  </section>
</div>
</body>
</html>
```